Flyer-Gestaltung für Pelz- & Gold-Ankauf
Zielgruppe
Pelz & Gold Ankauf Wendtner in Ottobrunn
Unsere Zielgruppe sind Rentner und Senioren
Wir kaufen Pelze Gold und Bernstein auf
Aber Hauptsächlich geht es um den Pelzankauf
Daher suchen wir ein hochwertiges Design was direkt ins Auge fällt
Aufgabenstellung
Wir brauchen ein vertrauenswürdiges und gleich auffälliges Inserat mit sehr hochwertigen Bildern und kleinen seriösen Texten.
Der größte Teil der Werbung sollte für die Pelze sein und ein kleiner für Bernstein und Goldschmuck.
Folgende Vorgaben müssen berücksichtigt werden:
- 231mm breite und 324mm Höhe
- Hochformat in der Zeitung
Für den Text sind folgende Informationen zu integrieren:
Wichtig wäre das unsere Pelz Aktion gilt nur 4 - 6 Tage
Wir zahlen bis zu 10 000 für Pelze
Unser Ankauf ist in ganz Ottobrunn, Unterhaching, Feldmoching, Aying Brunthal, Germering, Garching und Umgebung
Information zu den Anhängen:
Das 1 Bild war unsere alte Anzeige von damals aber die nicht grade besonders ist
Das 2 Bild und 3 Bild wäre die Konkurrenz
Es sollte selbstverständlich in jedem Punkt besser ausschauen
Wir möchten nicht der Konkurrenz ähneln
Bild 4 wäre ein Design wo uns gut gefällt von einen Bernstein Ankauf
Es sollte direkt ins Auge fallen
Ich hoffe auf ein auffälliges besonderes Design das die Leute überzeugt lieber bei mir ihren Pelz zu verkaufen

```html
<!DOCTYPE html>
<html lang="de">
<head>
<meta charset="utf-8">
<title>Pelze &amp; Gold Ankauf – Sonderaktion</title>
<link href="https://fonts.googleapis.com/css2?family=Questrial&family=Open+Sans:wght@800&family=Arimo&display=swap" rel="stylesheet">
<style>
  :root {
    --amber: #D9964A;
    --gold-ring: #D4A838;
    --slate: #666666;
    --paper: #FFFFFF;
    --ink: #111111;
    --fur-light: #D9A867;
    --fur-dark: #8A5A34;
  }
  html, body { margin: 0; padding: 0; overflow: hidden; }
  body { width: 856px; height: 1200px; background: var(--paper); }
  .flyer {
    position: relative; width: 856px; height: 1200px; overflow: hidden;
    background: var(--paper); font-family: 'Questrial', sans-serif;
  }
  .fur-band {
    position: absolute; left: 0; width: 856px;
    background: linear-gradient(90deg, var(--fur-dark) 0%, var(--fur-light) 22%, #B07A45 40%, #E3C08E 62%, #A46B3C 80%, var(--fur-light) 100%);
  }
  .fur-band--top { top: 0; height: 103px; }
  .fur-band--bottom { top: 1116px; height: 84px; }
  .banner-title {
    position: absolute; left: 64px; top: 22px; margin: 0;
    font-family: 'Open Sans', sans-serif; font-weight: 800; font-size: 54px;
    line-height: 60px; color: var(--paper); letter-spacing: -0.5px;
  }
  .headline {
    position: absolute; left: 0; width: 842px; top: 124px; margin: 0;
    text-align: center; font-weight: 400; font-size: 68px; line-height: 80px;
    color: var(--amber); letter-spacing: 1px;
  }
  .subline {
    position: absolute; left: 0; width: 846px; top: 222px; margin: 0;
    text-align: center; font-size: 43px; line-height: 66px; color: var(--ink); font-weight: 400;
  }
  .slate-panel {
    position: absolute; left: 0; top: 497px; width: 856px; height: 619px; background: var(--slate);
  }
  .coat-visual {
    position: absolute; left: 123px; top: 345px; width: 225px; height: 333px;
    background: var(--amber); border-radius: 90px 90px 18px 18px;
  }
  .promo-flag {
    position: absolute; left: 386px; top: 392px; margin: 0;
    font-size: 49px; line-height: 60px; color: var(--amber); font-weight: 400; letter-spacing: 0.5px;
  }
  .duration {
    position: absolute; left: 400px; width: 410px; top: 550px; margin: 0;
    text-align: center; font-size: 38px; line-height: 50px; color: var(--amber); font-weight: 400;
  }
  .region {
    position: absolute; left: 390px; width: 462px; top: 608px; margin: 0;
    text-align: center; font-size: 23.5px; line-height: 34px; color: var(--paper);
  }
  .goods-circle {
    position: absolute; top: 726px; width: 126px; height: 126px; border-radius: 50%;
    border: 6px solid var(--gold-ring);
  }
  .goods-circle--fur { left: 393px; background: radial-gradient(circle, #C9935A, #7A4F2E); }
  .goods-circle--gold { left: 543px; background: radial-gradient(circle, #F5EFE3, #C9B48A); }
  .goods-circle--amber { left: 699px; background: radial-gradient(circle, #E59A2E 0%, #C2631A 35%, #FFFFFF 60%); }
  .sans-copy { font-family: 'Arimo', sans-serif; color: var(--paper); }
  .goods-line {
    position: absolute; left: 390px; width: 446px; top: 896px; margin: 0;
    text-align: center; font-size: 26px; line-height: 32px;
  }
  .service-copy {
    position: absolute; left: 396px; width: 432px; top: 958px; margin: 0;
    text-align: center; font-size: 24px; line-height: 34.5px;
  }
  .accent { color: var(--amber); }
  .offer-card {
    position: absolute; left: 73px; top: 698px; width: 304px; height: 502px; background: var(--paper);
  }
  .offer-lead {
    position: absolute; left: 9px; top: 12px; margin: 0; font-weight: 400;
    font-size: 30px; line-height: 45px; color: var(--ink);
  }
  .offer-lead span { display: block; padding-left: 7px; }
  .offer-body {
    position: absolute; left: 9px; top: 104px; width: 292px; margin: 0;
    font-size: 20.5px; line-height: 30.5px; color: var(--ink);
  }
  .drop-cap {
    float: left; font-size: 64px; line-height: 50px; height: 56px; margin: 4px 4px 0 -2px;
    color: var(--amber);
  }
</style>
</head>
<body>
<main class="flyer">
  <div class="fur-band fur-band--top" role="img" aria-label="Nahaufnahme von Pelz in Braun- und Goldtönen"></div>
  <h2 class="banner-title">Sonderaktion</h2>

  <h1 class="headline">PELZE &amp; GOLD ANKAUF</h1>
  <p class="subline">Wertschätzung &amp; Ankauf in<br>Ottobrun und Umgebung</p>

  <div class="slate-panel"></div>
  <div class="fur-band fur-band--bottom" role="img" aria-label="Nahaufnahme von Pelz in Braun- und Goldtönen"></div>

  <div class="coat-visual" role="img" aria-label="Illustration eines Pelzmantels mit großem Kragen"></div>
  <p class="promo-flag">SONDERAKTION!</p>

  <p class="duration">Nur 4-6 Tage</p>
  <p class="region">In ganz Ottobrunn, Unterhaching,<br>Feldmoching, Aying Brunthal, Germering,<br>Garching und Umgebung</p>

  <div class="goods-circle goods-circle--fur" role="img" aria-label="Foto von Pelz"></div>
  <div class="goods-circle goods-circle--gold" role="img" aria-label="Foto von Goldarmreifen"></div>
  <div class="goods-circle goods-circle--amber" role="img" aria-label="Foto eines Bernsteins"></div>

  <p class="goods-line sans-copy">Wir kaufen <span class="accent">Pelze</span>, <span class="accent">Gold</span> und <span class="accent">Bernstein</span></p>
  <p class="service-copy sans-copy">Wir bieten eine kostenlose<br><span class="accent">WERTSCHÄTZUNG</span> Ihrer Schätze,<br>sowie einen <span class="accent">BAR-ANKAUF</span> vor<br>ORT.</p>

  <section class="offer-card">
    <h3 class="offer-lead">Erhalten Sie<span>bis zu 10.000€</span></h3>
    <p class="offer-body"><span class="drop-cap">W</span>ir kaufen Ihre Schätze zum fairen Preis!<br>Sie haben einen Pelz geerbt oder möchten sich schon lange davon trennen? Nun könnte er sich als finanzielle Überaschung entpuppen. Je nach Farbe, Zustand und Art können Sie bis zu 10.000 € erwarten. Es empfiehlt sich daher in jedem Fall einen Fachmann aufzusuchen.</p>
  </section>
</main>
</body>
</html>
```